eBook cover and content: Unlock Courage Beyond Every Boundary

I teach a leadership program to companies that was developed at Brintale and now need an eBook cover and content design. This downloadable eBook will be offered online in exchange for prospects' contact details. It needs to be designed with a sophisticated, senior HR executive audience in mind. There are some assets that are available for you to work with including photographs, a logo device for the program, and a colour palette (same as Brintale's blue, green, yellow and red). Note that while the program was developed at Brintale it is NOT a Brintale product and I need to ensure that the eBook does not breach license guidelines. I have attached a very rough mockup of the content, images and graphic elements to help.

Target Market(s)

Senior business leaders and HR professionals.

Industry/Entity Type

Leadership

Font styles to use
Sans Serif

Requirements
Must have
• Keep it simple. Clean, contemporary, professional feel. This is a high-value decision for a company and needs to look modern, progressive and credible. Downloadable PDF. Easy to read and digest layout.
• Colours - see attached screenshot for red, blue, green, yellow ref. Additionally charcoal for most type and purple 330033 as extra colour is okay.
• Landscape format please.
Nice to have
• Plenty of white space.

```html
<!DOCTYPE html>
<html lang="en">
<head>
<meta charset="utf-8">
<title>Unlock Courage Beyond Every Boundary – eBook pages</title>
<link rel="stylesheet" href="https://fonts.googleapis.com/css2?family=Roboto:ital,wght@0,300;0,400;0,500;0,700;1,300&display=swap">
<style>
  :root {
    --backdrop: #dc4a3c;
    --accent: #e0473a;
    --paper: #ffffff;
    --ink: #6b6b6b;
    --ink-dark: #333333;
    --photo-top: #d9cde0;
    --photo-mid: #b8a3a8;
    --photo-low: #6f5a5c;
  }
  * { box-sizing: border-box; margin: 0; padding: 0; }
  html, body { width: 1200px; height: 874px; overflow: hidden; }
  body {
    background: var(--backdrop);
    font-family: "Roboto", Arial, sans-serif;
    color: var(--ink);
    position: relative;
  }
  .page {
    position: absolute;
    width: 574px;
    height: 398px;
    background: var(--paper);
    box-shadow: 0 2px 6px rgba(0,0,0,.25);
    overflow: hidden;
  }
  .page--cover { left: 16px; top: 24px; }
  .page--reviews { left: 609px; top: 24px; }
  .page--help { left: 16px; top: 450px; }
  .page--featured { left: 609px; top: 450px; }

  .cover-photo {
    position: absolute; inset: 0;
    background: linear-gradient(180deg, var(--photo-top) 0%, #cdb9c6 35%, var(--photo-mid) 60%, var(--photo-low) 100%);
  }
  .page-title {
    position: absolute;
    left: 20px; top: 60px;
    font-weight: 300;
    font-size: 19px;
    line-height: 22px;
    letter-spacing: .3px;
    color: var(--accent);
    text-transform: uppercase;
  }
  .page-title::after {
    content: "";
    display: block;
    width: 60px; height: 3px;
    background: var(--accent);
    margin-top: 10px;
  }

  .running-head {
    position: absolute; left: 20px; top: 21px;
    display: flex; align-items: center; gap: 5px;
    font-size: 7px; color: var(--ink-dark);
  }
  .running-head .mark { width: 7px; height: 7px; border-radius: 50%; background: var(--accent); }

  .folio {
    position: absolute; right: 10px; bottom: 14px;
    font-size: 7px; color: var(--accent);
  }
  .folio::after {
    content: ""; position: absolute; right: -10px; top: -3px;
    width: 7px; height: 13px; background: var(--accent);
  }

  /* reviews */
  .reviews { position: absolute; left: 200px; top: 68px; width: 342px; }
  .review { display: flex; gap: 8px; margin-bottom: 13px; }
  .review-source {
    width: 40px; flex: none;
    font-size: 7.5px; font-weight: 500; color: var(--ink-dark);
    padding-top: 10px;
  }
  .review-quote {
    font-style: italic; font-weight: 300; font-size: 8.5px; line-height: 10.5px;
  }
  .review-by {
    display: block; font-size: 6px; color: var(--accent); margin-top: 3px;
  }
  .client-grid {
    position: absolute; left: 200px; top: 238px;
    display: grid; grid-template-columns: repeat(3, 110px); row-gap: 26px;
  }
  .client {
    display: flex; align-items: center; justify-content: center; gap: 4px;
    font-size: 9.5px; font-weight: 500; color: var(--ink-dark); height: 18px;
  }
  .client .dot { width: 8px; height: 8px; border-radius: 50%; background: var(--ink-dark); }
  .client .sq { width: 8px; height: 8px; background: var(--accent); }

  /* help */
  .help-copy {
    position: absolute; left: 200px; top: 63px; width: 340px;
    font-weight: 300; font-size: 8.5px; line-height: 11px;
  }
  .help-copy p { margin-bottom: 5px; }

  /* featured */
  .features { position: absolute; left: 200px; top: 61px; width: 350px; }
  .feature { margin-bottom: 20px; }
  .feature-name {
    font-size: 10px; font-weight: 700; color: var(--ink-dark);
    line-height: 11px; margin-bottom: 8px;
  }
  .feature--first .feature-name { margin-bottom: 19px; }
  .feature-quote {
    font-style: italic; font-weight: 300; font-size: 8.3px; line-height: 11px;
  }
  .read-more { display: block; font-size: 6px; line-height: 7px; color: var(--accent); margin-top: 6px; text-decoration: none; }
</style>
</head>
<body>

<section class="page page--cover">
  <div class="cover-photo" role="img" aria-label="Photograph of workshop participants chatting in a crowded event room"></div>
  <h1 class="page-title">Unlock your<br>full potential</h1>
</section>

<section class="page page--reviews">
  <div class="running-head"><span class="mark"></span>Inner Compass Leadership</div>
  <h2 class="page-title">Recent<br>participants<br>and reviews</h2>
  <div class="reviews">
    <div class="review">
      <div class="review-source">Brintale</div>
      <p class="review-quote">"ICL has had a tremendous impact on me and my team. We're clear, calmer and sharper for it and we're playing together nicely. Many of the practices are woven into our daily lives."<span class="review-by">Mara Lindqvist, Creative Director, Brintale Creative Lab</span></p>
    </div>
    <div class="review">
      <div class="review-source">Harbourline</div>
      <p class="review-quote">"The concepts are simple, accessible and translatable and made a huge impression on our emergency department team. I wholeheartedly recommend this program."<span class="review-by">Dr Anika Sethi, Harbourline Hospital, Emergency Department</span></p>
    </div>
    <div class="review">
      <div class="review-source">Veldrop</div>
      <p class="review-quote">"ICL has been the training highlight of the year at Veldrop. All participants have reported significant improvement in their professional and personal lives."<span class="review-by">Owen Larkin, People and Development Director, Veldrop</span></p>
    </div>
  </div>
  <div class="client-grid">
    <div class="client"><span class="dot"></span>Northbay</div>
    <div class="client">Kestrel</div>
    <div class="client">Orbisa</div>
    <div class="client">Pellow</div>
    <div class="client">Tamaru</div>
    <div class="client">Parcelo</div>
    <div class="client"><span class="sq"></span>Hartwell</div>
    <div class="client">Solvane</div>
    <div class="client">Eastvale</div>
  </div>
  <div class="folio">11</div>
</section>

<section class="page page--help">
  <div class="running-head"><span class="mark"></span>Inner Compass Leadership</div>
  <h2 class="page-title">We'd love to<br>help you</h2>
  <div class="help-copy">
    <p>Boost performance. Enhance leadership. Elevate wellbeing.</p>
    <p>We believe in amplifying human potential with powerful, evidence-based principle and practices.</p>
    <p>We've had the privilege to teach ICL to some of Australia's hottest startups, as well as global tech giants and manufacturers.</p>
    <p>We've taught international retail and investment banks, multinational media companies and telcos.</p>
    <p>And we've taught at hospitals, holding companies, universities and professional services firms.</p>
    <p>We'd love to help you too.</p>
    <p>Click one of these buttons and tell us more about you, your organisation and your leadership development goals.</p>
  </div>
  <div class="folio">10</div>
</section>

<section class="page page--featured">
  <div class="running-head"><span class="mark"></span>Inner Compass Leadership</div>
  <h2 class="page-title">Featured in</h2>
  <div class="features">
    <div class="feature feature--first">
      <div class="feature-name">Meridian<br>Business Review</div>
      <p class="feature-quote">'You know you could be a much more effective leader if you could approach each meeting with a fresh perspective. But in order to do that, you first need to put down the baggage you carried in from all your previous meetings. You can do it. And you can do it in just six seconds.'</p>
      <a class="read-more" href="#">&lt;&lt; read more</a>
    </div>
    <div class="feature">
      <div class="feature-name">SWIFT VENTURE</div>
      <p class="feature-quote">'Since the initial curriculum was developed specifically for Brintale's engineers, it needed to be taught in a completely straightforward, secular language, explains Hollis, because scientists and engineers are typically skeptics. The course focuses on what's happening in the brain when you're having certain thoughts and feelings, and encourages reflection rather than reaction.'</p>
      <a class="read-more" href="#">&lt;&lt; read more</a>
    </div>
    <div class="feature">
      <div class="feature-name">CRESTLINE<br>JOURNAL</div>
      <p class="feature-quote">'For me, the class was a much-needed opportunity to stop running, chewing, and cursing, and really notice what was happening — both around and inside me. Below, I've rounded up the insights from ICL that most resonated with me.'</p>
      <a class="read-more" href="#">&lt;&lt; read more</a>
    </div>
  </div>
  <div class="folio">13</div>
</section>

</body>
</html>
```